Classic and neutral book cover design

We are looking for a classic and neutral book cover design to be used as the template for a series of books to be published. We are hence looking for a template that will allow us to easily change the title name for all books in this series.
The use of very few colours (black and white is welcome) and few design elements is a big bonus. As a source of inspiration we would like to ask you to view the very simple and
If you think you have a cool idea that can add a twist to the formal classic look don't hesitate. Go for it !
Work will be done for a 30 year old Sweden based cultural non-profit called VĂ©ru (www.veruhaus-example.org). We work with the publishing and supporting of post-modern art and literature addressing contemporary topics but are also involved in assisting projects of cultural preservation.
Target Market(s)
The audience is expected to have some form of interest in culture but could range from hobbyist readers to tenure track scholars
Industry/Entity Type
Non-Profit
Requirements
Must have
- General:
- Classic and neutral feel
- Preferably very simple and few shapes
- usage of few colours (black and white is welcome)
Information to be displayed on the cover is:
- Author
- Title
- type of work e.g. play/novel (optional)
- publishing house (in this case "Veru Publishing")
Nice to have
- ideas to prevent it from become boring are of course welcome
Should not have
- - too many colours

```html
<!DOCTYPE html>
<html lang="en">
<head>
<meta charset="utf-8">
<title>Book Cover – Veru Publishing</title>
<link rel="stylesheet" href="https://fonts.googleapis.com/css2?family=Anton&family=Oswald:wght@600;700&family=Marcellus&display=swap">
<style>
  :root {
    --backdrop: #bdbdbd;
    --paper: #ffffff;
    --band: #9a9a9a;
    --band-type: #b3b3b3;
    --author: #8a8a8a;
    --title: #000000;
    --imprint: #222222;
  }
  html, body {
    margin: 0;
    padding: 0;
    width: 1200px;
    height: 812px;
    overflow: hidden;
    background: var(--backdrop);
  }
  .stage {
    position: relative;
    width: 1200px;
    height: 812px;
  }
  .cover {
    position: absolute;
    left: 341px;
    top: 81px;
    width: 518px;
    height: 650px;
    background: var(--paper);
    box-shadow: 6px 6px 6px rgba(0, 0, 0, 0.35);
  }
  .genre-band {
    position: absolute;
    left: 0;
    top: 0;
    width: 126px;
    height: 100%;
    background: var(--band);
  }
  .genre-band svg {
    display: block;
    width: 126px;
    height: 650px;
  }
  .genre-label {
    font-family: "Anton", "Oswald", sans-serif;
    font-size: 108px;
    fill: var(--band-type);
  }
  .heading {
    position: absolute;
    right: 27px;
    top: 127px;
    text-align: right;
  }
  .author {
    margin: 0;
    font-family: "Oswald", sans-serif;
    font-weight: 600;
    font-size: 20px;
    line-height: 26px;
    color: var(--author);
  }
  .title {
    margin: 2px 0 0;
    font-family: "Oswald", sans-serif;
    font-weight: 700;
    font-size: 42px;
    line-height: 46px;
    letter-spacing: -0.5px;
    color: var(--title);
  }
  .imprint {
    position: absolute;
    right: 27px;
    bottom: 16px;
    margin: 0;
    font-family: "Marcellus", serif;
    font-size: 15px;
    color: var(--imprint);
  }
</style>
</head>
<body>
  <main class="stage">
    <article class="cover">
      <div class="genre-band">
        <svg viewBox="0 0 126 650" aria-label="Play">
          <text class="genre-label" x="0" y="0"
                transform="translate(107 538) rotate(-90)"
                textLength="412" lengthAdjust="spacing">PLAY</text>
        </svg>
      </div>
      <header class="heading">
        <p class="author">Anders Lindqvist</p>
        <h1 class="title">Miss Ingrid</h1>
      </header>
      <p class="imprint">Veru Publishing</p>
    </article>
  </main>
</body>
</html>
```